Auto Body Repair Damage Postcard

We need a postcard to be used as handouts that sell customers on our brand and helps generate leads to our new Auto Body Repair Shop. Our shop colors are Black, Red, and White. On the back of the postcard, we would like to have an aerial view of a car on one side that we can mark in red brivlo as to where damage is located on the car along with our QR code that links to our mobile estimate app.

Target Market(s)

Customers that care about their vehicles and want them to look the best.

Other font styles liked:
• Montserrate

Requirements
Must have
• On the back of the postcard, we would like to have an aerial view of a car on one side that we can mark in red brivlo as to where damage is located on the car along with our QR code that links to our mobile estimate app. With a heading that says we noticed that you have a scratch/auto body damage.

```html
<!DOCTYPE html>
<html lang="en">
<head>
<meta charset="utf-8">
<title>Halvern Auto Rebuild – Postcard</title>
<link href="https://fonts.googleapis.com/css2?family=Bebas+Neue&family=Saira+Semi+Condensed:wght@400&family=Teko:wght@600&family=Montserrat:wght@800&display=swap" rel="stylesheet">
<style>
  :root {
    --stage: #5f5f5f;
    --ink: #333132;
    --red: #e11d2a;
    --red-deep: #b5121b;
    --red-dark: #4a1014;
    --white: #ffffff;
    --black: #111315;
  }
  html, body { margin: 0; padding: 0; overflow: hidden; }
  body { width: 1200px; height: 801px; background: var(--stage); }
  .postcard { position: relative; width: 1200px; height: 801px; }
  .postcard-shapes { position: absolute; inset: 0; }

  .brand-name {
    position: absolute; left: 112px; top: 172px; width: 430px;
    text-align: center; color: var(--black);
    font-family: "Montserrat", sans-serif; font-weight: 800;
  }
  .brand-name .brand-main { display: block; font-size: 58px; letter-spacing: 4px; line-height: 1; }
  .brand-name .brand-sub { display: block; font-size: 17px; letter-spacing: 14px; margin-top: 10px; }

  .tagline {
    position: absolute; left: 130px; top: 312px; margin: 0;
    font-family: "Bebas Neue", sans-serif; font-size: 31px; line-height: 40px;
    color: var(--white); letter-spacing: 0.5px;
  }
  .tagline-follow {
    position: absolute; left: 266px; top: 442px; margin: 0;
    font-family: "Bebas Neue", sans-serif; font-size: 32px; font-style: italic;
    color: var(--black);
  }
  .trust-word, .team-word, .shop-name {
    position: absolute; margin: 0; font-family: "Teko", sans-serif; font-weight: 600; line-height: 1;
  }
  .trust-word { left: 111px; top: 532px; font-size: 36px; color: var(--white); }
  .team-word { left: 277px; top: 578px; font-size: 46px; color: var(--red); letter-spacing: 2px; }
  .shop-name {
    left: 72px; top: 640px; font-size: 60px; letter-spacing: 3px;
    background: linear-gradient(to bottom, var(--white) 0 48%, var(--red) 48% 100%);
    -webkit-background-clip: text; background-clip: text; color: transparent;
  }

  .services { position: absolute; left: 732px; top: 210px; width: 330px; }
  .services-title {
    margin: 0 0 10px; width: 255px; text-align: center; padding-left: 16px;
    font-family: "Bebas Neue", sans-serif; font-size: 40px; color: var(--white); letter-spacing: 1px;
  }
  .services-list { list-style: none; margin: 0; padding: 0; }
  .services-list li {
    position: relative; padding-left: 33px; height: 34.4px;
    font-family: "Saira Semi Condensed", sans-serif; font-size: 21px; letter-spacing: 1.6px;
    color: var(--white); line-height: 26px;
  }
  .services-list li::before {
    content: ""; position: absolute; left: 0; top: 8px; width: 11px; height: 11px; background: var(--red);
  }
</style>
</head>
<body>
<main class="postcard">
  <svg class="postcard-shapes" viewBox="0 0 1200 801" width="1200" height="801" aria-hidden="true">
    <defs>
      <linearGradient id="band-fade" x1="0" x2="1" y1="0" y2="0">
        <stop offset="0" stop-color="var(--red-dark)"/>
        <stop offset="0.28" stop-color="var(--red-deep)"/>
        <stop offset="1" stop-color="var(--red-deep)"/>
      </linearGradient>
    </defs>
    <rect class="card-base" x="54" y="35" width="1092" height="734" fill="var(--ink)" stroke="var(--red)" stroke-width="2"/>
    <path class="sky-panel" d="M540,60 L1146,35 L1146,94 C1070,170 1000,230 900,270 L585,330 L585,75 Z" fill="var(--white)"/>
    <path class="hero-panel" d="M54,110 C250,70 450,72 540,75 C590,200 600,330 580,390 C555,500 470,555 395,548 C290,540 190,480 130,405 L54,405 Z" fill="var(--white)"/>
    <path class="hero-edge" d="M540,75 C590,200 600,330 580,390 C555,500 470,555 395,548 C290,540 190,480 130,405" fill="none" stroke="var(--red)" stroke-width="2"/>
    <path class="top-band" d="M54,35 L835,35 C700,60 620,75 540,76 C380,78 200,80 54,110 Z" fill="url(#band-fade)"/>
    <path class="tagline-pill" d="M54,289 L447,289 A58,58 0 0 1 447,406 L54,406 Z" fill="var(--ink)" stroke="var(--red)" stroke-width="2"/>
    <path class="tagline-ticks" d="M447,281 A66,66 0 0 1 447,413" fill="none" stroke="var(--red)" stroke-width="5" stroke-dasharray="3 7"/>
    <circle class="services-ring" cx="893" cy="341" r="206" fill="var(--ink)" stroke="var(--red)" stroke-width="6"/>
    <rect class="bottom-band" x="54" y="718" width="1092" height="48" fill="url(#band-fade)"/>
  </svg>

  <div class="brand-name">
    <span class="brand-main">HALVERN</span>
    <span class="brand-sub">AUTO REBUILD</span>
  </div>

  <p class="tagline">IT IS NOT OFTEN YOU NEED<br>AN AUTO BODY SHOP</p>
  <p class="tagline-follow">BUT WHEN YOU DO</p>
  <p class="trust-word">TRUST</p>
  <p class="team-word">TEAM</p>
  <p class="shop-name">HALVERN AUTO REBUILD</p>

  <section class="services">
    <h2 class="services-title">OUR SERVICES</h2>
    <ul class="services-list">
      <li>collision repairs</li>
      <li>Corvane frame equipment</li>
      <li>BUMPER REPAIR</li>
      <li>collision repairs</li>
      <li>Corvane frame equipment</li>
      <li>BUMPER REPAIR</li>
      <li>collision repairs</li>
      <li>Corvane frame equipment</li>
      <li>BUMPER REPAIR</li>
      <li>collision repairs</li>
      <li>Corvane frame equipment</li>
      <li>BUMPER REPAIR</li>
    </ul>
  </section>
</main>
</body>
</html>
```